Hollowpine Studio

I need business Cards with my logo and a background photo of one of my taxidermy mounts.
I would like a black back drop behind it all and what ever looks best for my contact information (red or white?)
Marcus Pellow
555-218-4907
hello@hollowpinestudio.net
Chatterly page

```html
<!DOCTYPE html>
<html lang="en">
<head>
<meta charset="utf-8">
<title>Hollowpine Studio — Business Cards</title>
<link rel="stylesheet" href="https://fonts.googleapis.com/css2?family=Open+Sans:wght@400;700&display=swap">
<style>
  :root {
    --backdrop: #2b2b2b;
    --card-black: #1c1c1d;
    --card-black-raised: #2e2e30;
    --card-white: #ffffff;
    --ink: #111111;
    --accent-red: #e3262b;
  }
  * { box-sizing: border-box; margin: 0; padding: 0; }
  html, body {
    width: 1200px; height: 900px; overflow: hidden;
    background: var(--backdrop);
    font-family: "Open Sans", Arial, sans-serif;
  }
  .canvas { position: relative; width: 1200px; height: 900px; }
  .card {
    position: absolute; left: 300px;
    width: 600px; height: 343px;
    overflow: hidden;
  }
  .card-back {
    top: 70px;
    background: var(--card-black);
    display: flex; align-items: center; justify-content: center;
  }
  .back-brand {
    font-weight: 700; font-size: 44px; letter-spacing: 4px;
    color: var(--card-black-raised); text-transform: uppercase;
    text-align: center; line-height: 1.15;
  }
  .card-front { top: 475px; background: var(--card-white); }
  .front-swoosh { position: absolute; inset: 0; width: 600px; height: 343px; }
  .holder-name {
    position: absolute; left: 60px; top: 40px;
    font-weight: 700; font-size: 22px; color: var(--accent-red);
    text-transform: uppercase; letter-spacing: 0.3px;
  }
  .contact-list {
    position: absolute; left: 58px; top: 110px;
    list-style: none; font-size: 17px; color: var(--ink);
  }
  .contact-list li { display: flex; align-items: center; gap: 10px; height: 26px; }
  .contact-icon { width: 16px; height: 16px; flex: none; }
  .front-brand {
    position: absolute; right: 40px; top: 100px;
    display: flex; align-items: center; gap: 12px;
    font-weight: 700; font-size: 26px; line-height: 1.15; color: var(--ink);
    text-transform: uppercase; letter-spacing: 1.5px;
  }
  .brand-square { width: 20px; height: 20px; background: var(--ink); flex: none; }
  .social {
    position: absolute; left: 24px; bottom: 50px;
    display: flex; align-items: center; gap: 8px;
    font-size: 14px; color: var(--card-white);
  }
  .social-square { width: 14px; height: 14px; background: var(--card-white); }
</style>
</head>
<body>
<main class="canvas">
  <section class="card card-back">
    <p class="back-brand">Hollowpine<br>Studio</p>
  </section>

  <section class="card card-front">
    <svg class="front-swoosh" viewBox="0 0 600 343" aria-hidden="true">
      <path d="M0,228 C160,232 380,312 600,330 L600,343 L0,343 Z" fill="var(--card-black)"/>
      <path d="M110,248 C290,300 450,318 600,312 L600,324 C450,330 290,312 110,248 Z" fill="var(--accent-red)"/>
    </svg>

    <h1 class="holder-name">Marcus Pellow</h1>

    <ul class="contact-list">
      <li>
        <svg class="contact-icon" viewBox="0 0 16 16" aria-hidden="true">
          <path d="M3.5,1 L6,1 L7,4.5 L5.3,5.7 C6.2,7.7 8.3,9.8 10.3,10.7 L11.5,9 L15,10 L15,12.5 C15,13.9 13.9,15 12.5,15 C6.5,14.5 1.5,9.5 1,3.5 C1,2.1 2.1,1 3.5,1 Z" fill="var(--accent-red)"/>
        </svg>
        <span>555-218-4907</span>
      </li>
      <li>
        <svg class="contact-icon" viewBox="0 0 16 16" aria-hidden="true">
          <rect x="0.5" y="3" width="15" height="10" fill="var(--accent-red)"/>
          <path d="M0.5,3 L8,9 L15.5,3" fill="none" stroke="#fff" stroke-width="1.2"/>
        </svg>
        <span>hello@hollowpinestudio.net</span>
      </li>
    </ul>

    <div class="front-brand">
      <span class="brand-square"></span>
      <span>Hollowpine<br>Studio</span>
    </div>

    <div class="social">
      <span class="social-square"></span>
      <span>Chatterly</span>
    </div>
  </section>
</main>
</body>
</html>
```